Website Re-design and extension of an existing website

I have a Wordpress website currently and I need it to be upgraded. I have MOST of the content to get it started and the rest (video's, pictures ect) are on the way. I want to know if it is possible to convert my existing website into a Personal Brand website with a public speaking emphasis. I would like to have my website modeled after the following website:

http://www.vandolake.example/

I have attached a document entitled "Website Outline & Content" that has all of the text on it and it has red headlines that indicate where something needs to be added or designed. I will be happy to give more detail if needed.

Things I still need to get to you in order to design the website;

-Demo video
-Full length public speaking video

Target Market(s)

Corporations, universities, trade associations, private events

Coding

Coded - Design and coding required

Requirements
Must have
• Pictures, links, downloadable forms, MULTIPLE video's embedded, my logo, keep the colors in sync with my existing marketing material
Nice to have
• I would like my design colors thematic as already inherent in my marketing materials (see my Speaker One Sheet)

```html
<!DOCTYPE html>
<html lang="en">
<head>
<meta charset="utf-8">
<title>Brett Harlow – Holistic Lifestyle Hacker</title>
<link href="https://fonts.googleapis.com/css2?family=Oswald:wght@400;500;600&family=Open+Sans:wght@400;600;700&display=swap" rel="stylesheet">
<style>
:root{
  --olive:#74744a;
  --olive-dark:#5e5f3b;
  --ink:#222222;
  --text:#555555;
  --muted:#888888;
  --nav:#2a2a2a;
  --footer:#1d1d1b;
  --cream:#f1f0e8;
  --line:#d9d9d9;
  --white:#ffffff;
}
*{box-sizing:border-box;margin:0;padding:0}
html,body{width:1200px;height:3766px;overflow:hidden}
body{position:relative;background:var(--white);font-family:"Open Sans",Arial,sans-serif;color:var(--text)}
.abs{position:absolute}
.oswald{font-family:"Oswald","Arial Narrow",sans-serif}

/* header */
.site-header{left:0;top:0;width:1200px;height:98px;background:var(--white)}
.brand{left:100px;top:22px;display:flex;align-items:center;gap:12px}
.brand-dot{width:50px;height:50px;border-radius:50%;background:var(--olive)}
.brand-name{font-family:"Oswald",sans-serif;font-weight:600;font-size:34px;color:var(--olive-dark);letter-spacing:.5px;text-transform:uppercase}
.connect{right:100px;top:30px;display:flex;align-items:center;gap:10px;font-family:"Oswald",sans-serif;font-size:17px;color:var(--ink)}
.connect .social{width:36px;height:36px;border-radius:50%;border:2px solid #555}
.connect span{margin-right:10px}
.main-nav{left:0;top:98px;width:1200px;height:42px;background:var(--nav);display:flex;align-items:center;padding-left:112px;gap:34px;font-family:"Oswald",sans-serif;font-size:15px;color:var(--white)}
.main-nav .active{color:#d9cf8a}

/* hero */
.hero{left:0;top:140px;width:1200px;height:432px;background:linear-gradient(180deg,#8ea3b8 0%,#a99b86 45%,#6a5e4c 75%,#3c352c 100%)}
.hero-title{left:100px;top:250px;font-family:"Oswald",sans-serif;font-weight:500;font-size:50px;color:var(--white);text-transform:uppercase}
.hero-sub{left:100px;top:318px;font-family:"Oswald",sans-serif;font-size:28px;color:var(--white)}
.hero-btn{left:100px;top:390px;width:394px;height:52px;border:2px solid var(--white);border-radius:26px;color:var(--white);font-weight:700;font-size:15px;text-transform:uppercase;display:flex;align-items:center;justify-content:center}
.dots{display:flex;gap:6px}
.dots i{width:12px;height:12px;border-radius:50%;border:2px solid var(--white);display:block}
.dots i.on{background:var(--white)}
.hero .dots{position:absolute;left:570px;top:366px}

/* intro */
.intro-title{left:0;width:1200px;top:628px;text-align:center;font-family:"Oswald",sans-serif;font-size:34px;line-height:53px;color:var(--ink)}
.pill{height:60px;width:251px;border:2px solid #bbb;border-radius:30px;display:flex;align-items:center;justify-content:center;text-align:center;font-weight:700;font-size:14px;line-height:18px;color:var(--olive-dark);text-transform:uppercase;top:773px}

/* sugar */
.sugar{left:0;top:916px;width:1200px;height:459px;background:var(--cream)}
.section-title{left:0;width:1200px;text-align:center;font-family:"Oswald",sans-serif;font-size:34px;color:var(--ink)}
.impact{width:240px;text-align:center;top:1060px}
.impact .ring{width:164px;height:164px;border:3px solid var(--olive-dark);border-radius:50%;margin:0 auto;display:flex;align-items:center;justify-content:center}
.impact p{margin-top:36px;font-size:18px;line-height:29px;font-weight:600;color:var(--ink)}

/* knowledge */
.know-title{left:100px;top:1440px;font-family:"Oswald",sans-serif;font-size:35px;color:var(--ink)}
.know-copy{left:100px;top:1505px;width:490px;font-size:14px;line-height:27px;color:var(--text)}
.know-copy p+p{margin-top:27px}
.outline-btn{border:2px solid #999;border-radius:20px;display:flex;align-items:center;justify-content:center;font-weight:700;font-size:13px;color:var(--olive-dark);text-transform:uppercase}
.video{left:630px;top:1451px;width:470px;height:301px;background:linear-gradient(180deg,#9fb8cc 0%,#e9d7a8 45%,#6e8796 70%,#3f5663 100%);border:5px solid #e4e4e4}
.play{left:204px;top:119px;width:60px;height:60px;border-radius:50%;background:#1b1b1b}

/* testimonials */
.testi{left:0;top:1877px;width:1200px;height:332px;background:linear-gradient(135deg,#8a7d6e 0%,#5b5045 50%,#2e2925 100%)}
.testi-label{left:100px;top:152px;font-family:"Oswald",sans-serif;font-size:32px;color:var(--white)}
.avatar{left:577px;top:40px;width:102px;height:102px;border-radius:50%;background:linear-gradient(180deg,#c9c9c9,#8d8d8d);border:4px solid var(--white)}
.quote{left:577px;top:163px;width:525px;font-style:italic;font-size:15px;line-height:24px;color:#eeeeee}
.cite{left:577px;top:264px;font-weight:700;font-size:14px;color:#eeeeee;text-transform:uppercase}
.testi .dots{position:absolute;left:1058px;top:278px}
.testi .dots i{width:11px;height:11px}

/* press */
.press-card{top:2369px;width:322px}
.press-img{width:322px;height:184px}
.press-card h3{margin-top:48px;font-size:18px;line-height:27px;font-weight:600;color:var(--ink)}
.meta{margin-top:12px;font-size:12px;color:var(--text);display:flex;align-items:center;gap:7px}
.meta b{display:inline-block;width:11px;height:11px;background:var(--ink)}
.excerpt{margin-top:12px;font-size:13px;line-height:23px;color:var(--text)}
.readmore{margin-top:12px;font-weight:700;font-size:13px;color:var(--olive-dark);text-transform:uppercase}
.rule{left:100px;top:2829px;width:1000px;height:1px;background:var(--line)}
.client{top:2962px;width:176px;height:83px;border:2px solid var(--line);display:flex;align-items:center;justify-content:center;font-size:22px;font-weight:600;color:#8a8a8a}

/* cta */
.cta{left:0;top:3135px;width:1200px;height:90px;background:var(--olive-dark)}
.cta-text{left:100px;top:28px;font-family:"Oswald",sans-serif;font-size:23px;color:var(--white)}
.cta-btn{left:963px;top:20px;width:137px;height:48px;border:2px solid var(--white);border-radius:24px;color:var(--white);font-weight:700;font-size:15px;display:flex;align-items:center;justify-content:center;text-transform:uppercase}

/* footer */
.footer{left:0;top:3225px;width:1200px;height:541px;background:var(--footer)}
.totop{left:560px;top:35px;width:80px;text-align:center;color:var(--white);font-weight:700;font-size:13px}
.foot-h{font-family:"Oswald",sans-serif;font-size:22px;color:var(--white)}
.field{background:var(--white);height:34px;font-size:11px;color:#777;padding:9px 10px}
.submit{left:617px;top:408px;width:109px;height:34px;border-radius:17px;background:#8f8b5e;color:var(--white);font-weight:700;font-size:13px;display:flex;align-items:center;justify-content:center;text-transform:uppercase}
.info-row{left:778px;display:flex;align-items:center;gap:26px;font-size:14px;color:#dddddd}
.info-ic{width:34px;height:34px;border-radius:50%;background:#2f2f2c;display:flex;align-items:center;justify-content:center}
.foot-social{left:778px;top:370px;display:flex;gap:8px}
.foot-social i{display:block;width:30px;height:30px;border-radius:50%;background:var(--olive)}
.foot-rule{left:100px;top:460px;width:1000px;height:1px;background:#3a3a37}
.copyright{left:0;width:1200px;top:495px;text-align:center;font-size:12px;color:#cccccc}
</style>
</head>
<body>

<header class="site-header abs">
  <div class="brand abs"><span class="brand-dot"></span><span class="brand-name">Brett Harlow</span></div>
  <div class="connect abs"><span>Connect with Brett Harlow:</span><i class="social"></i><i class="social"></i><i class="social"></i><i class="social"></i></div>
</header>
<nav class="main-nav abs">
  <span class="active">Home</span><span>About Brett Harlow</span><span>Keynote</span><span>Workshop Presenter</span><span>Author</span><span>Coaching</span><span>Blog</span><span>Online Courses</span><span>Contact Brett Harlow</span>
</nav>

<section class="hero abs" role="img" aria-label="Photo of the speaker smiling, leaning on a wooden railing with mountains behind">
  <div class="dots"><i class="on"></i><i></i><i></i><i></i></div>
</section>
<h1 class="hero-title abs">Brett Harlow</h1>
<p class="hero-sub abs">Sugar Addiction Expert, Holistic Health Expert, Author &amp; Speaker</p>
<div class="hero-btn abs">See how Brett Harlow can help you</div>

<h2 class="intro-title abs">Your Holistic Lifestyle Hacker<br>Lose Your Mind &amp; Find Your Health!</h2>
<div class="pill abs" style="left:193px">Download Brett's<br>Speaker One Sheet</div>
<div class="pill abs" style="left:477px">Download Brett's<br>Media Sheet</div>
<div class="pill abs" style="left:758px">Download Brett's College<br>Speaker One Sheet</div>

<section class="sugar abs"></section>
<h2 class="section-title abs" style="top:975px">Sugar Addiction (The Stealth Addiction) is destroying:</h2>
<div class="impact abs" style="left:81px">
  <div class="ring"><svg width="80" height="64" viewBox="0 0 80 64"><g fill="#5e5f3b"><rect x="8" y="36" width="10" height="22"/><rect x="24" y="24" width="10" height="34"/><rect x="40" y="30" width="10" height="28"/><rect x="56" y="10" width="10" height="48"/></g><path d="M2 4V62H78" stroke="#5e5f3b" stroke-width="4" fill="none"/></svg></div>
  <p>Your<br>bottom-line</p>
</div>
<div class="impact abs" style="left:347px">
  <div class="ring"><svg width="60" height="60" viewBox="0 0 60 60"><polygon fill="#5e5f3b" points="30,2 36,12 47,8 47,20 58,24 51,33 58,42 47,45 46,57 35,53 30,58 24,52 13,57 12,45 2,42 9,33 2,24 13,20 13,8 24,12"/></svg></div>
  <p>Your Insurance<br>Premiums</p>
</div>
<div class="impact abs" style="left:613px">
  <div class="ring"><svg width="74" height="60" viewBox="0 0 74 60"><g fill="#5e5f3b"><circle cx="37" cy="14" r="10"/><circle cx="14" cy="20" r="8"/><circle cx="60" cy="20" r="8"/><path d="M20 58V40a17 14 0 0 1 34 0v18z"/><path d="M0 52V42a14 12 0 0 1 18-10v20z"/><path d="M74 52V42a14 12 0 0 0-18-10v20z"/></g></svg></div>
  <p>The health of<br>your employees</p>
</div>
<div class="impact abs" style="left:877px">
  <div class="ring"><svg width="50" height="66" viewBox="0 0 50 66"><rect x="3" y="3" width="44" height="60" fill="none" stroke="#5e5f3b" stroke-width="4"/><g fill="#5e5f3b"><rect x="11" y="11" width="8" height="7"/><rect x="21" y="11" width="8" height="7"/><rect x="31" y="11" width="8" height="7"/><rect x="11" y="23" width="8" height="7"/><rect x="21" y="23" width="8" height="7"/><rect x="31" y="23" width="8" height="7"/><rect x="11" y="35" width="8" height="7"/><rect x="21" y="35" width="8" height="7"/><rect x="31" y="35" width="8" height="7"/><rect x="20" y="48" width="10" height="15"/></g></svg></div>
  <p>The culture of<br>your company</p>
</div>

<h2 class="know-title abs">Without Your Knowledge Or Consent!</h2>
<div class="know-copy abs">
  <p>For over 17 years, Brett Harlow has tirelessly helped executives, employees, and everyday people achieve lasting health and fitness by helping them "lose their minds."</p>
  <p>Using his unique 4-Quadrant Coaching System, speaking platform, and online training courses, Brett has helped hundreds of people shed their limiting beliefs, eat better, shed sugar addiction and transform their bodies and minds.</p>
</div>
<div class="outline-btn abs" style="left:100px;top:1750px;width:130px;height:40px">Read More</div>
<div class="video abs" role="img" aria-label="Video still of a person with arms raised at sunrise beside a lake">
  <svg class="play abs" viewBox="0 0 60 60"><circle cx="30" cy="30" r="30" fill="#1b1b1b"/><polygon points="24,18 42,30 24,42" fill="#ffffff"/></svg>
</div>

<section class="testi abs" role="img" aria-label="Background photo of a rocky hillside under a dusky sky">
  <svg class="abs" style="left:0;top:0" width="600" height="332" viewBox="0 0 600 332"><polygon points="0,0 600,0 160,332 0,332" fill="#7a7a49" opacity=".92"/></svg>
  <svg class="abs" style="left:100px;top:50px" width="88" height="74" viewBox="0 0 88 74"><g fill="#ffffff"><path d="M0 40C0 18 10 4 30 0l3 8C22 12 17 20 17 30h17v44H0z"/><path d="M50 40C50 18 60 4 80 0l3 8C72 12 67 20 67 30h17v44H50z"/></g></svg>
  <div class="testi-label abs">Testimonials</div>
  <div class="avatar abs" role="img" aria-label="Portrait photo of the reviewer"></div>
  <p class="quote abs">Brett's program changed how our whole staff thinks about food. Energy is up, sick days are down, and the team keeps asking when he is coming back to speak again.</p>
  <div class="cite abs">- Marcus T. Delaney MD,PA</div>
  <div class="dots"><i class="on"></i><i></i><i></i></div>
</section>

<h2 class="section-title abs" style="top:2288px">Press</h2>
<article class="press-card abs" style="left:100px">
  <div class="press-img" role="img" aria-label="Photo of a man wrestling with a red lawn mower on grass" style="background:linear-gradient(180deg,#4f7a2c,#a33a2a 60%,#3f6a25)"></div>
  <h3>Why You Continue To Eat Junk Food Despite Your "Will Power"</h3>
  <div class="meta"><b></b>Dec 4th, 2017 &nbsp;|&nbsp; <b></b>Brett Harlow</div>
  <p class="excerpt">Has Our Modern Eating Habits Made It Impossible To Say "No" To Junk Food?</p>
  <div class="readmore">Read More</div>
</article>
<article class="press-card abs" style="left:440px">
  <div class="press-img" role="img" aria-label="Photo of a stressed woman holding her head" style="background:linear-gradient(180deg,#efeae6,#c89a7d 60%,#e6ddd6)"></div>
  <h3>3 Reasons Why You Are Not Losing Weight Long Term...</h3>
  <div class="meta"><b></b>Nov 22nd, 2017 &nbsp;|&nbsp; <b></b>Brett Harlow</div>
  <p class="excerpt">Hello my friends! How are you? I really hope that you had a great Thanksgiving!</p>
  <div class="readmore">Read More</div>
</article>
<article class="press-card abs" style="left:778px">
  <div class="press-img" role="img" aria-label="Photo of a woman with glasses laughing while eating a cupcake" style="background:linear-gradient(180deg,#d8c7a4,#c79274 55%,#e7ddcf)"></div>
  <h3>Filthy Mouth or Filthy Food? Challenging "Chosen" Societal Morals</h3>
  <div class="meta"><b></b>Sep 6th, 2017 &nbsp;|&nbsp; <b></b>Brett Harlow</div>
  <p class="excerpt">Picture this: You're walking down the street with your kids, laughing as you look at the clouds.</p>
  <div class="readmore">Read More</div>
</article>
<div class="rule abs"></div>

<h2 class="section-title abs" style="top:2875px">Our Clients</h2>
<div class="client abs" style="left:100px">Swiftline</div>
<div class="client abs" style="left:306px">Ambassa</div>
<div class="client abs" style="left:515px">Qorvana</div>
<div class="client abs" style="left:720px">Climb &amp; Co</div>
<div class="client abs" style="left:926px">StudyWorks</div>

<section class="cta abs">
  <p class="cta-text abs">Become a Holistic Health Hacker and receive a FREE 30-Day Meal Plan crafted by Brett!</p>
  <div class="cta-btn abs">Join Now!</div>
</section>

<footer class="footer abs">
  <svg class="abs" style="left:565px;top:8px" width="70" height="24" viewBox="0 0 70 24"><polygon points="0,24 20,0 50,0 70,24" fill="#3a3a37"/></svg>
  <div class="totop abs">TO TOP</div>
  <h3 class="foot-h abs" style="left:100px;top:132px">Contact form</h3>
  <div class="field abs" style="left:100px;top:201px;width:309px">Name :</div>
  <div class="field abs" style="left:417px;top:201px;width:309px">Phone no :</div>
  <div class="field abs" style="left:100px;top:255px;width:626px">Email :</div>
  <div class="field abs" style="left:100px;top:294px;width:626px;height:84px">Message :</div>
  <div class="submit abs">Submit</div>

  <h3 class="foot-h abs" style="left:778px;top:132px">Contact Information</h3>
  <div class="info-row abs" style="top:189px"><span class="info-ic"><svg width="14" height="18" viewBox="0 0 14 18"><path d="M7 0a7 7 0 0 1 7 7c0 5-7 11-7 11S0 12 0 7a7 7 0 0 1 7-7z" fill="#fff"/><circle cx="7" cy="7" r="2.5" fill="#2f2f2c"/></svg></span>412 Alder Grove Rd Portland ME 04101</div>
  <div class="info-row abs" style="top:247px"><span class="info-ic"><svg width="16" height="16" viewBox="0 0 16 16"><path d="M3 0l3 4-2 2c1 2 4 5 6 6l2-2 4 3-2 3C7 16 0 9 0 3z" fill="#fff"/></svg></span>1 888 888 8888</div>
  <div class="info-row abs" style="top:302px"><span class="info-ic"><svg width="16" height="12" viewBox="0 0 16 12"><rect width="16" height="12" fill="#fff"/><path d="M0 0l8 7 8-7" stroke="#2f2f2c" stroke-width="1.5" fill="none"/></svg></span>info@bretharlow.example</div>
  <div class="foot-social abs"><i></i><i></i><i></i><i></i></div>
  <div class="foot-rule abs"></div>
  <p class="copyright abs">Copyright © 2017, Brett Harlow. All rights reserved.</p>
</footer>

</body>
</html>
```